TRENDY & MODERN BUSINESS CARD DESIGN for Media Company *

I need a minimalistic - clean - modern and professional business card layout and design for MEDIA & PHOTOGRAPHY STUDIO.

We do NOT have a logo, and not really looking for one - but rather excellent typography and design. We would consider the 3 as a focal point.

We do personal and commercial photography.

Target Market(s)

Personal and commercial photography clientele

Contact Information for Business Card

ZUB size - from zub.com / size guidelines are enclosed in the brief

Font styles to use
Sans Serif

Colors
f78f20
eda3c7
cee9f5
0555a3
e667a6
fbf289

Requirements
Must have
• Clean lines - Modern layout
Nice to have
• All blue background as an option - use color palette in brief please.
Should not have
• Old fashion fonts and regular fonts.

```html
<!DOCTYPE html>
<html lang="en">
<head>
<meta charset="utf-8">
<title>Northlight Media — Business Card</title>
<link href="https://fonts.googleapis.com/css2?family=Work+Sans:wght@400;500;600&display=swap" rel="stylesheet">
<style>
  :root {
    --backdrop: #d6dadb;
    --card-front: #f1f0ec;
    --card-back: #262626;
    --ink: #1c1c1c;
    --ink-soft: #333333;
    --emboss: #4c4c4c;
    --rule: #1c1c1c;
  }
  * { margin: 0; padding: 0; box-sizing: border-box; }
  html, body {
    width: 1200px; height: 900px; overflow: hidden;
    background: var(--backdrop);
    font-family: "Work Sans", sans-serif;
    color: var(--ink);
  }
  .canvas { position: relative; width: 1200px; height: 900px; }
  .card {
    position: absolute; left: 270px;
    width: 660px; height: 377px;
    overflow: hidden;
  }
  .card--front { top: 48px; background: var(--card-front); }
  .card--back { top: 475px; background: var(--card-back); }

  .person { position: absolute; left: 44px; top: 62px; }
  .person__name {
    font-size: 21px; font-weight: 500; letter-spacing: 0.12em; text-transform: uppercase;
  }
  .person__role {
    margin-top: 6px; font-size: 14px; letter-spacing: 0.14em; color: var(--ink-soft);
  }
  .front-rule {
    position: absolute; left: 44px; top: 140px; width: 520px; height: 1px; background: var(--rule);
  }

  .brand { position: absolute; text-align: left; }
  .brand--front { right: 40px; top: 62px; }
  .brand__name {
    font-size: 21px; font-weight: 500; letter-spacing: 0.1em; white-space: nowrap;
  }
  .brand__rule { height: 1px; background: var(--rule); margin: 8px 0 6px; }
  .brand__tagline {
    font-size: 12px; letter-spacing: 0.1em; white-space: nowrap; color: var(--ink-soft);
  }

  .details {
    position: absolute; font-size: 12.5px; line-height: 1.55;
    letter-spacing: 0.06em; color: var(--ink-soft); font-style: normal;
  }
  .details--contact { left: 44px; top: 178px; }
  .details--address { left: 250px; top: 228px; }
  .details--locations { left: 400px; top: 290px; }

  .brand--back {
    left: 50%; top: 50%; transform: translate(-50%, -50%); color: var(--emboss);
  }
  .brand--back .brand__name { font-size: 34px; font-weight: 600; }
  .brand--back .brand__rule { background: var(--emboss); margin: 10px 0 8px; }
  .brand--back .brand__tagline { font-size: 18px; color: var(--emboss); }
</style>
</head>
<body>
<main class="canvas">
  <section class="card card--front" aria-label="Business card front">
    <div class="person">
      <h1 class="person__name">Marisol Vega</h1>
      <p class="person__role">Founder &amp;Media Director</p>
    </div>
    <div class="front-rule"></div>

    <div class="brand brand--front">
      <p class="brand__name">NORTHLIGHT MEDIA</p>
      <div class="brand__rule"></div>
      <p class="brand__tagline">Framing Moments.&nbsp; Making Memories.</p>
    </div>

    <address class="details details--contact">
      (305) 555-0142<br>mv@northlightmedia.com
    </address>
    <address class="details details--address">
      240 Harbor Avenue<br>9th Floor Miami, FL 33130
    </address>
    <p class="details details--locations">
      Locations: Tampa • Boston •<br>Denver • Tulum • Lisboa
    </p>
  </section>

  <section class="card card--back" aria-label="Business card back">
    <div class="brand brand--back">
      <p class="brand__name">NORTHLIGHT MEDIA</p>
      <div class="brand__rule"></div>
      <p class="brand__tagline">Framing Moments.&nbsp; Making Memories.</p>
    </div>
  </section>
</main>
</body>
</html>
```